Need a brochure design for my business which sells Australian themed Christmas ornaments.

We need a brochure designed for our company called Wattle Glow Pty Ltd.
Our company sells Australian themed glass Christmas ornaments which have been internally hand painted with designs depicting Australian flora & fauna as well as Indigenous art designs. Our website, www.wattleglow.com.au will show you the product we sell. We would like a brochure to display our current designs (19 in total). Six of the designs have a front & back image. Each design image will be accompanied with a short description of what the design represents. The ornaments each present with a padded gift box for storage and a descriptive swing tag.
We would like to use the same colours of our website (blue and yellow) and would like to incorporate the company logo. We would like the brochure to communicate that all designs have been reproduced from commissioned art work by Australian Indigenous and non-Indigenous artists. The descriptive words unique, Australian, quality, keepsake, gift and beautiful should all be used.
Our website and contact details are also to be included. (See attached files for reference).
The brochure will be distributed to both wholesale and retail clients..

Target Market(s)

Wholesale and retail gift shop clients

Industry/Entity Type

Retail

Requirements
Must have
• All 19 designs must be depicted. All design descriptions must be included. An image example of the padded gift box and swing tag must be included.
The company Logo must be used, preferably at the top of the page.
Must state that all designs have been reproduced from commissioned artwork by Australian Indigenous and non-Indigenous artists.
The descriptive words: Australian design, unique, internally hand-painted, gift, keepsake and beautiful must be used.
The blue and yellow colours (as depicted on the website) must be used. Ideally the brochure would be a two page document (front and back) of one sheet but I will leave the size up to you depending on the design.
Website and contact details.

```html
<!DOCTYPE html>
<html lang="en">
<head>
<meta charset="utf-8">
<title>Wattle Glow – Ornament Brochure</title>
<link href="https://fonts.googleapis.com/css2?family=Mulish:ital,wght@0,600;0,800;1,700&display=swap" rel="stylesheet">
<style>
:root{
  --orange:#e8891a;
  --blue:#1c63d6;
  --frame:#2a4fb8;
  --white:#ffffff;
  --paper:#ffffff;
}
*{box-sizing:border-box;margin:0;padding:0}
html,body{width:1200px;height:1000px;overflow:hidden;background:var(--paper)}
body{font-family:"Mulish",sans-serif}
.sheet{position:absolute;left:250px;top:20px;display:grid;grid-template-columns:340px 340px;grid-template-rows:470px 470px;gap:20px}
.panel{position:relative;background:var(--orange);box-shadow:4px 4px 8px rgba(0,0,0,.25);overflow:hidden}
.panel::before,.panel::after{content:"";position:absolute;top:8px;bottom:8px;border-left:2px dotted rgba(255,255,255,.85)}
.panel::before{left:7px}
.panel::after{right:7px}
.cover::before,.cover::after{top:198px}

/* cover */
.cover-top{height:190px;background:var(--white);display:flex;align-items:center;justify-content:center}
.brand{display:flex;align-items:center;gap:10px}
.brand-dot{width:22px;height:22px;border-radius:50%;background:var(--blue)}
.brand-name{font-weight:800;font-size:30px;color:var(--blue);letter-spacing:1px}
.cover-body{padding:22px 30px 0;text-align:center;color:var(--blue);font-weight:800;font-size:11px;line-height:1.35}
.cover-body p{margin-bottom:12px}

/* product rows */
.rows{padding:12px 18px 0 16px;display:flex;flex-direction:column;gap:6px}
.row{display:flex;align-items:center;gap:10px;height:55px}
.thumb{flex:0 0 150px;height:52px;background:var(--white);border:1.5px solid var(--frame);padding:3px;transform:rotate(-2deg)}
.row:nth-child(even) .thumb{transform:rotate(1.8deg)}
.thumb span{display:block;width:100%;height:100%}
.info{flex:1;text-align:center}
.info h3{color:var(--white);font-weight:800;font-size:9.5px;letter-spacing:.3px;text-transform:uppercase;margin-bottom:2px}
.info p{color:var(--blue);font-weight:800;font-size:7.5px;line-height:1.25}
.back .row{height:58px}
.back .thumb{height:55px}

.statement{padding:12px 24px 0;text-align:center;color:var(--blue);font-style:italic;font-weight:700;font-size:9.5px;line-height:1.3}
.contact{padding-top:8px;text-align:center;color:var(--blue);font-weight:800;font-size:11px;line-height:1.3}
</style>
</head>
<body>
<main class="sheet">

  <section class="panel cover">
    <div class="cover-top">
      <div class="brand"><span class="brand-dot"></span><span class="brand-name">wattle glow</span></div>
    </div>
    <div class="cover-body">
      <p>Proud to produce a unique range of HAND-PAINTED glass ornaments. The designs are reproduced exclusively for Wattle Glow Pty Ltd.</p>
      <p>Our current range includes:<br>unique, gift,<br>Australian designs,<br>internally hand-painted,<br>keepsake and beautiful.</p>
      <p>WATTLE GLOW<br>PO BOX 2290, BRISBANE, QLD, 4000</p>
      <p>PH: +61-7-3000 4127<br>FAX: +61-7-3000 4128<br>www.wattleglow.com.au</p>
    </div>
  </section>

  <section class="panel back">
    <div class="rows">
      <div class="row"><div class="thumb"><span role="img" aria-label="Pink Chorus ornament, front and back views" style="background:linear-gradient(90deg,#a9c9d6,#e88fb4,#a9c9d6)"></span></div>
        <div class="info"><h3>Pink Chorus</h3><p>A noisy flock of rosy-chested birds chattering across the open plains at dusk.</p></div></div>
      <div class="row"><div class="thumb"><span role="img" aria-label="Big Foot Bounder ornament, front and back views" style="background:linear-gradient(90deg,#c6d6a8,#d9c49a,#c6d6a8)"></span></div>
        <div class="info"><h3>Big Foot Bounder</h3><p>Strong legs and a long tail carry this marsupial in great leaps through the bush.</p></div></div>
      <div class="row"><div class="thumb"><span role="img" aria-label="Wild Howl ornament, front and back views" style="background:linear-gradient(90deg,#7cc0d6,#e0b04a,#7cc0d6)"></span></div>
        <div class="info"><h3>Wild Howl</h3><p>A golden wild dog whose lonely howl echoes over the sandhills at night.</p></div></div>
      <div class="row"><div class="thumb"><span role="img" aria-label="Sulphur Crest ornament, front and back views" style="background:linear-gradient(90deg,#a7d8d6,#eef2e8,#a7d8d6)"></span></div>
        <div class="info"><h3>Sulphur Crest</h3><p>A white bird with a bright yellow crest, living in pairs or in loud, busy flocks.</p></div></div>
      <div class="row"><div class="thumb"><span role="img" aria-label="Red Centre ornament, front and back views" style="background:linear-gradient(90deg,#e2dccb,#d98a4a,#e2dccb)"></span></div>
        <div class="info"><h3>Red Centre</h3><p>A great rock rising from the desert, glowing red and gold at sunrise and sunset.</p></div></div>
    </div>
    <p class="statement">All designs have been reproduced from commissioned artwork by Australian Indigenous and non-Indigenous artists.</p>
    <p class="contact">PH: +61-7-3000 4127<br>FAX: +61-7-3000 4128<br>www.wattleglow.com.au</p>
  </section>

  <section class="panel inside-left">
    <div class="rows">
      <div class="row"><div class="thumb"><span role="img" aria-label="Resting Python ornaments" style="background:linear-gradient(90deg,#d8c3a5,#b52a2a,#d8c3a5)"></span></div>
        <div class="info"><h3>Resting Python</h3><p>Her long journey over, she curls up beneath the warm earth to rest.</p></div></div>
      <div class="row"><div class="thumb"><span role="img" aria-label="Gathering Rings ornaments" style="background:linear-gradient(90deg,#2233c8,#4a66e6,#2233c8)"></span></div>
        <div class="info"><h3>Gathering Rings</h3><p>Families meeting together,<br>circle within circle.</p></div></div>
      <div class="row"><div class="thumb"><span role="img" aria-label="Ember Trails ornaments" style="background:linear-gradient(90deg,#cc1a1a,#e84a4a,#cc1a1a)"></span></div>
        <div class="info"><h3>Ember Trails</h3><p>Campfire sparks lighting the many roads our people walk.</p></div></div>
      <div class="row"><div class="thumb"><span role="img" aria-label="Red Earth Runner ornaments" style="background:linear-gradient(90deg,#c9c21a,#5a8a2a,#c9c21a)"></span></div>
        <div class="info"><h3>Red Earth Runner</h3><p>A tall bird who cannot fly, racing swiftly over the dry plains.</p></div></div>
      <div class="row"><div class="thumb"><span role="img" aria-label="Desert Keeper ornaments" style="background:linear-gradient(90deg,#c2b01a,#a8421a,#c2b01a)"></span></div>
        <div class="info"><h3>Desert Keeper</h3><p>Watcher of the sands, hiding deep under the sun-baked ground.</p></div></div>
      <div class="row"><div class="thumb"><span role="img" aria-label="Dawn Shoal ornaments" style="background:linear-gradient(90deg,#6de0b0,#4a5ac8,#6de0b0)"></span></div>
        <div class="info"><h3>Dawn Shoal</h3><p>Silver fish darting through the first light of morning.</p></div></div>
      <div class="row"><div class="thumb"><span role="img" aria-label="River Swirl ornaments" style="background:linear-gradient(90deg,#e36fc9,#c23aa8,#e36fc9)"></span></div>
        <div class="info"><h3>River Swirl</h3><p>Spinning, turning.<br>Eddies play along the riverbank.</p></div></div>
    </div>
  </section>

  <section class="panel inside-right">
    <div class="rows">
      <div class="row"><div class="thumb"><span role="img" aria-label="Sunrise Song ornaments" style="background:linear-gradient(90deg,#e82525,#f25a5a,#e82525)"></span></div>
        <div class="info"><h3>Sunrise Song</h3><p>Morning light spreads across the country, wrapping us in its warmth.</p></div></div>
      <div class="row"><div class="thumb"><span role="img" aria-label="Shell Memory ornaments" style="background:linear-gradient(90deg,#d9b77a,#c29a5a,#d9b77a)"></span></div>
        <div class="info"><h3>Shell Memory</h3><p>Old shell mounds tell the stories of those before us.</p></div></div>
      <div class="row"><div class="thumb"><span role="img" aria-label="Billabong Guardian ornaments" style="background:linear-gradient(90deg,#2f5e1e,#7a2a1a,#2f5e1e)"></span></div>
        <div class="info"><h3>Billabong Guardian</h3><p>Old protector of<br>the quiet waterhole.</p></div></div>
      <div class="row"><div class="thumb"><span role="img" aria-label="Hatchling Journey ornaments" style="background:linear-gradient(90deg,#3fa6c9,#2a5a8a,#3fa6c9)"></span></div>
        <div class="info"><h3>Hatchling Journey</h3><p>A tiny turtle making the long trip from the sand to the sea.</p></div></div>
      <div class="row"><div class="thumb"><span role="img" aria-label="Flowing Waters ornaments" style="background:linear-gradient(90deg,#8fd0c4,#5aa8a0,#8fd0c4)"></span></div>
        <div class="info"><h3>Flowing Waters</h3><p>Rushing streams, calm lagoons and rolling sea waves.</p></div></div>
      <div class="row"><div class="thumb"><span role="img" aria-label="Estuary Giant ornaments" style="background:linear-gradient(90deg,#b9dbe6,#7aa88a,#b9dbe6)"></span></div>
        <div class="info"><h3>Estuary Giant</h3><p>A huge reptile lying in wait in the warm tidal rivers of the far north.</p></div></div>
      <div class="row"><div class="thumb"><span role="img" aria-label="Gum Tree Sleeper ornaments" style="background:linear-gradient(90deg,#c7dfe6,#8a9aa8,#c7dfe6)"></span></div>
        <div class="info"><h3>Gum Tree Sleeper</h3><p>A furry tree dweller who dozes all day and dines on gum leaves.</p></div></div>
    </div>
  </section>

</main>
</body>
</html>
```